First North America Product Category Rule

8 x 10 foot booth design for a stretch fabric wrap-around. The booth will be used in a very small exhibit area for 150 attendees. It is for the packaging industry focused on the environment. This booth graphic is NOT about our company, but to promote participation in a project we are sponsoring. The project is to develop the first North American Packaging Category Rule, so the booth is to invite conference attendees to join our effort. Production specifications are attached.

Target Market(s)

Zenith 400, Sustainability Directors, Packaging Engineers

Industry/Entity Type

Packaging; Environment

Font styles to use
Sans Serif

Requirements
Must have
• An Eye-Catching or Intriguing Image/Graphics/Letter Treatment
Should not have
• Nothing too bright or garish. All text should be above waist height (No text below the 36-40" mark)

```html
<!DOCTYPE html>
<html lang="en">
<head>
<meta charset="utf-8">
<title>Enlisting Stakeholder Participation – PCR for Protective Packaging</title>
<link href="https://fonts.googleapis.com/css2?family=Oswald:wght@600;700&family=Montserrat:wght@500;700;800&display=swap" rel="stylesheet">
<style>
  :root{
    --stage:#d9d9d9;
    --paper:#f4f4f4;
    --navy:#27487c;
    --brown:#4f281c;
    --green:#00a651;
    --orange:#f07c10;
    --orange-light:#f8a046;
    --gold:#b98a10;
    --gold-dark:#9c7208;
    --petal-1:#5ec10a;
    --petal-2:#4ea500;
    --petal-3:#367505;
    --petal-4:#2a5e08;
    --white:#ffffff;
  }
  *{box-sizing:border-box;margin:0;padding:0}
  html,body{width:1200px;height:756px;overflow:hidden;background:var(--stage)}
  .banner{
    position:absolute;left:0;top:39px;width:1200px;height:678px;overflow:hidden;
    background:linear-gradient(120deg,#f8f8f8 0%,#ececec 55%,#f6f6f6 100%);
    font-family:"Montserrat",sans-serif;color:var(--white);
  }
  .backdrop{position:absolute;inset:0}
  .title{
    position:absolute;left:0;width:100%;top:40px;text-align:center;
    font-family:"Oswald",sans-serif;font-weight:700;font-size:44px;letter-spacing:.5px;
    color:var(--navy);text-shadow:3px 3px 0 var(--white),4px 4px 2px rgba(0,0,0,.15);
  }
  .headline{
    position:absolute;left:328px;top:100px;width:545px;height:64px;
    background:var(--brown);border-radius:10px 10px 0 0;
    font-family:"Oswald",sans-serif;font-weight:700;font-size:50px;line-height:64px;text-align:center;
  }
  .subhead{
    position:absolute;left:237px;top:165px;width:727px;height:49px;
    background:var(--green);border-radius:10px 0 10px 0;
    font-weight:700;font-size:23px;line-height:49px;text-align:center;letter-spacing:.3px;
  }
  .cta{
    position:absolute;left:453px;top:225px;width:293px;height:51px;border-radius:26px;
    background:linear-gradient(180deg,var(--orange-light),var(--orange) 55%,#e06a00);
    border:2px solid #d8630a;
    font-weight:800;font-size:30px;line-height:47px;text-align:center;letter-spacing:.5px;
  }
  .steps{position:absolute;left:228px;top:284px;width:291px;height:291px}
  .petal{position:absolute;width:141px;height:141px;font-weight:700;font-size:13.5px;line-height:15px}
  .petal-1{left:0;top:0;background:var(--petal-1);border-radius:70px 70px 0 70px}
  .petal-2{left:150px;top:0;background:var(--petal-2);border-radius:70px 70px 70px 0}
  .petal-4{left:0;top:150px;background:var(--petal-4);border-radius:70px 0 70px 70px}
  .petal-3{left:150px;top:150px;background:var(--petal-3);border-radius:0 70px 70px 70px}
  .petal-label{position:absolute;border-left:1.5px solid var(--white);padding-left:4px}
  .petal-1 .petal-label{left:37px;top:42px}
  .petal-2 .petal-label{left:27px;top:49px}
  .petal-4 .petal-label{left:27px;top:43px}
  .petal-3 .petal-label{left:29px;top:47px}
  .petal-num{position:absolute;font-weight:700;font-size:20px}
  .petal-1 .petal-num{right:10px;bottom:8px}
  .petal-2 .petal-num{left:8px;bottom:8px}
  .petal-4 .petal-num{right:10px;top:8px}
  .petal-3 .petal-num{left:8px;top:8px}
  .quote{
    position:absolute;left:822px;top:235px;width:168px;height:168px;border-radius:50%;
    background:var(--gold);text-align:center;padding-top:46px;
    font-weight:700;font-size:10px;line-height:13.4px;
  }
  .quote-ring{position:absolute;left:812px;top:225px;width:188px;height:188px;border-radius:50%;border:1.5px solid var(--orange)}
  .quote-mark{position:absolute;left:0;width:100%;font-family:"Oswald",sans-serif;font-size:44px;line-height:1}
  .quote-mark.open{top:4px}
  .quote-mark.close{bottom:-22px}
  .credits{
    position:absolute;left:197px;top:585px;width:807px;height:49px;background:var(--brown);
    border-radius:0 0 10px 10px;font-weight:500;font-size:17px;line-height:49px;text-align:center;
  }
  .credits strong{font-weight:700}
  .credits .divider{margin:0 16px}
</style>
</head>
<body>
<main class="banner">
  <svg class="backdrop" width="1200" height="678" viewBox="0 0 1200 678">
    <defs>
      <linearGradient id="warehouse" x1="0" y1="0" x2="1" y2="1">
        <stop offset="0" stop-color="#c9a37a"/>
        <stop offset=".45" stop-color="#a9a9a4"/>
        <stop offset=".75" stop-color="#8d96a2"/>
        <stop offset="1" stop-color="#c7b49a"/>
      </linearGradient>
      <linearGradient id="swoosh" x1="0" y1="0" x2="1" y2="0">
        <stop offset="0" stop-color="var(--gold)"/>
        <stop offset="1" stop-color="var(--gold-dark)"/>
      </linearGradient>
    </defs>
    <path role="img" aria-label="Photo of a warehouse worker in a safety vest using a laptop among shelves of boxes"
      d="M0,556 C150,585 350,555 500,470 C650,385 790,305 960,318 C1080,330 1160,370 1200,420 L1200,678 L0,678 Z"
      fill="url(#warehouse)"/>
    <path d="M0,388 C120,470 260,485 420,405 C600,318 800,268 980,282 L980,302 C800,300 650,372 500,460 C350,548 150,572 0,538 Z"
      fill="url(#swoosh)"/>
    <path d="M0,546 C150,580 350,552 500,468 C650,382 800,302 980,308" fill="none" stroke="var(--white)" stroke-width="4"/>
  </svg>

  <h1 class="title">ENLISTING STAKEHOLDER PARTICIPATION</h1>
  <div class="headline">FIRST NORTH AMERICAN</div>
  <div class="subhead">Product Category Rule (PCR) For Protective Packaging</div>
  <div class="cta">SIGN UP NOW</div>

  <section class="steps">
    <div class="petal petal-1"><div class="petal-label">PCR<br>Product<br>Category<br>Rules</div><span class="petal-num">01</span></div>
    <div class="petal petal-2"><div class="petal-label">LCA<br>Life Cycle<br>Assessment</div><span class="petal-num">02</span></div>
    <div class="petal petal-4"><div class="petal-label">EDP<br>Registration<br>and<br>Publication</div><span class="petal-num">04</span></div>
    <div class="petal petal-3"><div class="petal-label">Third<br>Party<br>Verification</div><span class="petal-num">03</span></div>
  </section>

  <div class="quote-ring"></div>
  <blockquote class="quote">
    <span class="quote-mark open">“</span>
    How EPD Can Move the<br>Dialogue Beyond<br>End-of-Life Disposal to<br>Include Environmental<br>Benchmarks for<br>Product Production &amp;<br>Distribution
    <span class="quote-mark close">”</span>
  </blockquote>

  <footer class="credits">Sponsored by- <strong>Cellular Pack Guild</strong><span class="divider">|</span>Managed by- <strong>Open Ledger Builders</strong></footer>
</main>
</body>
</html>
```